PostCard Design Project

I am making a mailing postcard
I am having the mailing printed using 4 color foil on certain parts.
I am looking for a design that maximizes the foil process where certain parts are done in foil to grab the customers attention (example: if there is a car on the postcard the headlights would be done in foil) .
I am targeting some industries, (auto, real estate, medical, beauty) I would like the post card to have examples of postcard ideas for 2 or 3 of these industries.
specs:
the postcard should be atleast 6.5x9 up to 8.5x11, I don't want to restrict the space for the creative as I don't want everything to look like a huge mess. both sides will be used.
the piece is a direct mail piece so it has to meet requirements of https://www.parcelvane-post.com/business/pdf/quick-reference-guide.pdf
text will be
"business with no limits, meet mailing with no addresses, gain new customers through "Whole Route Flyer Drop" reach new customers at their home without needing their address. "
I also want some current print specials I am running included.
-double your order FREE (order 500 business cards and get 1000)
-250 100lb gloss stock brochures 99.00
-business packages (cards, envelopes and letterhead) 299
-1000 flyers 140.40
-5000 postcards 179.99
A list of services
banners
booklets
brochures
business cards
calendars
catalogs
CD/DVD packages
envelopes
event tickets
flyers
hangtags
postcards
posters
presentation folders
rack cards
labels
table tents
window cling and decal
"order 24/7 orders@cardwillow.com" must be included
my logo is CardWillow will be supplied later
ive received some great designs. however Im looking for something a little more modern like some zelkor would put out. if the amount of words is too much please feel free to edit. also an idea i had for the list of services i offer is to have it transparent yet readable as the background of the postcard some small some big but covering the entire backgroud. you can then design on top of that with other thing. just an early morning thought
Reason: I have uploaded a sketch of my idea, please take time to look at it for an accurate depiction of what im looking for. feel free to add elements that make it pop off the page
Reason: We are getting close i will be providing feed back today
Business

```html
<!DOCTYPE html>
<html lang="en">
<head>
<meta charset="utf-8">
<title>CardWillow Services Mailer</title>
<link rel="stylesheet" href="https://fonts.googleapis.com/css2?family=Source+Sans+3:wght@400;600;700;800;900&display=swap">
<style>
  :root {
    --red-deep: #9e0008;
    --red: #d8121b;
    --red-bright: #ef2a2a;
    --ink: #111111;
    --graphite: #3c3c3c;
    --silver: #d9d9d9;
    --white: #ffffff;
    --gold: #f4c542;
    --orange: #f39a1e;
    --text-dark: #1a1a1a;
    --logo-blue: #2f8fd8;
  }
  * { margin: 0; padding: 0; box-sizing: border-box; }
  html, body { width: 1200px; height: 927px; overflow: hidden; background: #ffffff; }
  .mailer {
    position: relative;
    width: 1200px;
    height: 927px;
    overflow: hidden;
    font-family: "Source Sans 3", Arial, sans-serif;
    color: var(--white);
  }
  .mailer-backdrop { position: absolute; inset: 0; }

  .services-title {
    position: absolute;
    left: 40px;
    top: 18px;
    font-size: 84px;
    font-weight: 900;
    letter-spacing: 1px;
    line-height: 1;
    background: linear-gradient(180deg, #ffe066 0%, var(--gold) 40%, var(--orange) 100%);
    -webkit-background-clip: text;
    background-clip: text;
    color: transparent;
    filter: drop-shadow(3px 4px 3px rgba(0,0,0,0.55));
  }
  .services-list {
    position: absolute;
    top: 128px;
    list-style: none;
    font-size: 27px;
    font-weight: 700;
    line-height: 44px;
    text-shadow: 1px 2px 2px rgba(0,0,0,0.45);
  }
  .services-list--left { left: 30px; }
  .services-list--right { left: 312px; }

  .postage-indicia {
    position: absolute;
    left: 1016px;
    top: 8px;
    width: 174px;
    height: 140px;
    background: var(--white);
    border: 2px solid var(--ink);
    color: var(--text-dark);
    font-size: 17px;
    line-height: 21px;
    text-align: center;
    padding-top: 14px;
  }

  .offer {
    position: absolute;
    text-align: center;
    font-weight: 700;
    line-height: 1;
    text-shadow: 2px 3px 3px rgba(0,0,0,0.5);
  }
  .offer-item { font-size: 41px; letter-spacing: -0.5px; }
  .offer-price { font-size: 64px; font-weight: 700; letter-spacing: -1px; }
  .offer-price sup { font-size: 28px; vertical-align: 30px; }
  .offer-price .cents { font-size: 30px; vertical-align: 28px; }
  .offer--flyers { left: 690px; top: 204px; width: 316px; }
  .offer--flyers .offer-price { margin: 4px 0 14px; }
  .offer--packages { left: 830px; top: 538px; width: 340px; }
  .offer--packages .offer-item { font-size: 38px; }
  .offer-note { font-size: 22px; margin: 4px 0 6px; }

  .address-block {
    position: absolute;
    left: 700px;
    top: 798px;
    width: 300px;
    height: 102px;
    background: var(--white);
    border: 2px solid var(--ink);
    color: var(--text-dark);
    font-size: 17px;
    line-height: 20px;
    padding: 10px 0 0 14px;
  }
  .address-block .endorsement { text-align: center; padding-right: 14px; margin-bottom: 20px; }

  .brand-mark {
    position: absolute;
    left: 1013px;
    top: 798px;
    width: 158px;
    height: 102px;
    background: var(--white);
    border: 2px solid var(--ink);
    display: flex;
    flex-direction: column;
    align-items: center;
    justify-content: center;
    gap: 8px;
  }
  .brand-dot { width: 30px; height: 30px; border-radius: 50%; background: var(--logo-blue); }
  .brand-name { font-size: 25px; font-weight: 600; color: var(--logo-blue); }
</style>
</head>
<body>
<main class="mailer">
  <svg class="mailer-backdrop" width="1200" height="927" viewBox="0 0 1200 927" aria-hidden="true">
    <defs>
      <linearGradient id="red-field" x1="0" y1="0" x2="1" y2="1">
        <stop offset="0" stop-color="#e8141c"/>
        <stop offset="0.55" stop-color="#c90d15"/>
        <stop offset="1" stop-color="#8c0006"/>
      </linearGradient>
      <linearGradient id="dark-field" x1="1" y1="0" x2="0" y2="1">
        <stop offset="0" stop-color="#6a6a6a"/>
        <stop offset="0.35" stop-color="#2a2a2a"/>
        <stop offset="1" stop-color="#0a0a0a"/>
      </linearGradient>
      <linearGradient id="silver-band" x1="0" y1="0" x2="1" y2="0">
        <stop offset="0" stop-color="#ffffff"/>
        <stop offset="0.6" stop-color="#e6e6e6"/>
        <stop offset="1" stop-color="#9a9a9a"/>
      </linearGradient>
      <radialGradient id="oval-fill" cx="0.45" cy="0.35" r="0.7">
        <stop offset="0" stop-color="#f03030"/>
        <stop offset="1" stop-color="#a4000a"/>
      </radialGradient>
      <linearGradient id="home-scene" x1="0" y1="0" x2="0" y2="1">
        <stop offset="0" stop-color="#9aa27c"/>
        <stop offset="0.45" stop-color="#c9b99a"/>
        <stop offset="1" stop-color="#4f6a34"/>
      </linearGradient>
    </defs>

    <rect width="1200" height="927" fill="url(#red-field)"/>
    <path d="M700,0 H1200 V470 C1050,470 860,520 700,600 C650,420 640,190 700,0 Z" fill="url(#dark-field)"/>
    <path d="M690,430 C850,390 1030,360 1200,350 V382 C1030,392 860,420 695,470 Z" fill="url(#silver-band)" opacity="0.9"/>
    <path d="M700,320 C880,300 1040,290 1200,300 V318 C1040,312 880,322 702,346 Z" fill="#bfbfbf" opacity="0.55"/>
    <path d="M705,490 C860,455 1020,440 1200,440 V470 C1040,470 880,500 712,540 Z" fill="#f2b7c3" opacity="0.75"/>
    <path d="M672,576 C700,700 700,820 676,927 H740 C760,820 760,690 720,560 Z" fill="#1a0002" opacity="0.55"/>

    <path d="M0,576 H672 C690,700 694,820 676,927 H0 Z" fill="url(#home-scene)" role="img" aria-label="Photo of a family standing in front of their newly bought house with a sold sign"/>

    <ellipse cx="848" cy="311" rx="167" ry="145" fill="url(#oval-fill)" stroke="var(--gold)" stroke-width="5"/>
    <ellipse cx="1000" cy="612" rx="176" ry="104" fill="url(#oval-fill)" stroke="var(--gold)" stroke-width="5"/>
  </svg>

  <h1 class="services-title">SERVICES</h1>
  <ul class="services-list services-list--left">
    <li>Banners</li>
    <li>Booklets</li>
    <li>Brochures</li>
    <li>Business Cards</li>
    <li>Calendars</li>
    <li>Catalogs</li>
    <li>CD/DVD packages</li>
    <li>Envelopes</li>
    <li>Event tickets</li>
  </ul>
  <ul class="services-list services-list--right">
    <li>Flyers</li>
    <li>Hangtags</li>
    <li>Postcards</li>
    <li>Posters</li>
    <li>Presentation Folders</li>
    <li>Rack Cards</li>
    <li>Labels</li>
    <li>Table Tents</li>
    <li>Window Cling &amp; Decal</li>
  </ul>

  <div class="postage-indicia">
    PRSRT STD<br>U.S. POSTAGE<br>PAID<br>CITY, STATE<br>PERMIT NO. XXX
  </div>

  <div class="offer offer--flyers">
    <div class="offer-item">1000 Flyers</div>
    <div class="offer-price"><sup>$</sup>140<span class="cents">40</span></div>
    <div class="offer-item">5000 Postcards</div>
    <div class="offer-price"><sup>$</sup>179<span class="cents">99</span></div>
  </div>

  <div class="offer offer--packages">
    <div class="offer-item">Business Packages</div>
    <div class="offer-note">(Cards, Envelopes &amp; Letterhead)</div>
    <div class="offer-price"><sup>$</sup>299<span class="cents">99</span></div>
  </div>

  <div class="address-block">
    <div class="endorsement">*********ECRWSSEDDM****</div>
    Postal Customer<br>City, State 5-Digit ZIP Code
  </div>

  <div class="brand-mark">
    <span class="brand-dot"></span>
    <span class="brand-name">CardWillow</span>
  </div>
</main>
</body>
</html>
```